Tobias Wrenfield - Cinematographer

NEED:
I'm looking for a sleek, professional, modern business card that will give give the recipient the impression that they can trust their production will go smoothly by hiring me. I will bring creativity and knowledge to their shoot, so that we can create powerful images.
I am looking for a card with a strong style and design ethos that could be expanded to a website and a full visual/graphic/design entity for me.
ABOUT ME:
I am a mid-twenties cinematographer, I work on music video, narrative short, commercial, and corporate projects. I blend the science and artistry of cameras and filmmaking to tell a story. I'm an artist, a technician, and a manager.
DESIGN:
I like sleek, simple design. Black, dark grays, white, dark navy, steel blues, I love cyan, but also cyan and red. I am not a fan of earthy tones. I generally prefer modern, san-serif fonts over serifs. My old logo was based on an aperture, a multi-blade device at the back of a lens that controls how much light passes through, but I made it with so many colors, that it doesn't necessarily lend itself to a specific color-scheme or design ethos. I liked that the aperture design provided a sense of the technical requirements of my job. I'm a fan of matte business cards, but am open to plenty of specialty print processes to make an outstanding card.
ATTACHED FILES:
My Old Rainbox Aperture Logo, plus a few designs I've tried playing around with, but am not tied to. I AM OPEN TO NEW DESIGNS, DO NOT FEEL TIED TO THIS.
**I've pulled my old logo down from the attached files, and instead attached other business cards I like, so as not to mislead you where I would like to go.
INFO:
Name: Tobias Wrenfield
Job: Cinematographer
Email: tkwrenfield@quillbox.example
Phone: 503.618.2907
Website: tobiaswrenfield.example
Updates
I'm adding some images of other cards that I like, and removing my old logo, since I'm looking for something new, and don't want that old logo to push anyone a certain direction.

```html
<!DOCTYPE html>
<html lang="en">
<head>
<meta charset="utf-8">
<title>Tobias Wrenfield – Cinematographer Business Card</title>
<link rel="stylesheet" href="https://fonts.googleapis.com/css2?family=Lato:wght@400;700;900&display=swap">
<style>
  :root {
    --page-bg: #dcdcdc;
    --blue-light: #1fb3ee;
    --blue-mid: #1384d6;
    --blue-dark: #0f58ad;
    --black: #050505;
    --white: #ffffff;
    --soft-white: rgba(255,255,255,0.92);
    --rule-cyan: rgba(120, 215, 255, 0.75);
  }
  * { box-sizing: border-box; margin: 0; padding: 0; }
  html, body {
    width: 1200px; height: 926px; overflow: hidden;
    background: var(--page-bg);
    font-family: "Lato", sans-serif;
  }
  .sheet {
    position: relative; width: 1200px; height: 926px;
  }
  .card {
    position: absolute; left: 280px; width: 640px; height: 366px;
    border-radius: 2px;
    box-shadow: 0 6px 18px rgba(0,0,0,0.22);
    overflow: hidden;
  }
  /* Front */
  .card--front {
    top: 60px;
    background: radial-gradient(ellipse 70% 80% at 45% 35%, var(--blue-light) 0%, var(--blue-mid) 48%, var(--blue-dark) 100%);
    color: var(--white);
  }
  .identity {
    position: absolute; left: 38px; top: 40px;
    display: flex; align-items: center; gap: 16px;
  }
  .identity__mark {
    width: 62px; height: 62px; border-radius: 50%;
    background: var(--white);
  }
  .identity__text { position: relative; }
  .identity__name {
    font-weight: 900; font-size: 38px; letter-spacing: -0.5px; line-height: 1;
  }
  .identity__role {
    display: block; text-align: right;
    font-size: 9px; font-weight: 700; letter-spacing: 1.6px; margin-top: 4px;
  }
  .website {
    position: absolute; left: 40px; top: 150px;
    font-size: 18px; display: flex; align-items: center; gap: 6px;
  }
  .rule {
    position: absolute; left: 0; top: 208px; width: 100%; height: 1px;
    background: linear-gradient(90deg, transparent 0%, var(--rule-cyan) 20%, var(--rule-cyan) 70%, transparent 100%);
  }
  .social {
    position: absolute; left: 40px; top: 188px; list-style: none;
    font-size: 16px;
  }
  .social li { display: flex; align-items: center; gap: 8px; margin-bottom: 4px; }
  .social__box {
    width: 12px; height: 12px; background: var(--soft-white); border-radius: 2px;
  }
  .contact {
    position: absolute; right: 36px; bottom: 40px; list-style: none;
    text-align: right; font-size: 18px;
  }
  .contact li { display: flex; justify-content: flex-end; align-items: center; gap: 10px; margin-top: 8px; }
  .contact__phone { font-size: 20px; letter-spacing: 0.5px; }
  /* Back */
  .card--back {
    top: 500px;
    background: radial-gradient(circle at 50% 45%, #1c1c1c 0%, var(--black) 40%);
  }
  .back__rule {
    position: absolute; left: 60px; right: 60px; top: 150px; height: 1px;
    background: linear-gradient(90deg, transparent, rgba(255,255,255,0.55) 45%, rgba(255,255,255,0.55) 55%, transparent);
  }
  .back__mark {
    position: absolute; left: 50%; top: 150px; width: 130px; height: 130px;
    margin: -65px 0 0 -65px; border-radius: 50%;
    background: var(--white);
    box-shadow: 0 0 30px rgba(255,255,255,0.25);
  }
  .back__name {
    position: absolute; left: 0; right: 0; top: 250px; text-align: center;
    color: var(--white); font-weight: 900; font-size: 22px;
  }
</style>
</head>
<body>
<main class="sheet">
  <section class="card card--front" aria-label="Business card front">
    <div class="identity">
      <span class="identity__mark"></span>
      <div class="identity__text">
        <span class="identity__name">Tobias Wrenfield</span>
        <span class="identity__role">CINEMATOGRAPHER</span>
      </div>
    </div>
    <p class="website">www.tobiaswrenfield.example
      <svg width="13" height="13" viewBox="0 0 14 14" aria-hidden="true">
        <circle cx="7" cy="7" r="6" fill="none" stroke="#fff" stroke-width="1.2"/>
        <ellipse cx="7" cy="7" rx="2.6" ry="6" fill="none" stroke="#fff" stroke-width="1"/>
        <line x1="1" y1="7" x2="13" y2="7" stroke="#fff" stroke-width="1"/>
      </svg>
    </p>
    <div class="rule"></div>
    <ul class="social" style="top:222px">
      <li><span class="social__box"></span>tobias.wrenfield</li>
      <li><span class="social__box"></span>tobias@wrenfield</li>
    </ul>
    <ul class="contact">
      <li>tkwrenfield@quillbox.example
        <svg width="15" height="11" viewBox="0 0 15 11" aria-hidden="true">
          <rect x="0.5" y="0.5" width="14" height="10" fill="#fff"/>
          <path d="M0.5 0.5 L7.5 6 L14.5 0.5" fill="none" stroke="#1470c4" stroke-width="1.2"/>
        </svg>
      </li>
      <li class="contact__phone">503.618.2907
        <svg width="12" height="18" viewBox="0 0 12 18" aria-hidden="true">
          <rect x="0.7" y="0.7" width="10.6" height="16.6" rx="1.5" fill="none" stroke="#fff" stroke-width="1.3"/>
          <rect x="2.5" y="3" width="7" height="9" fill="#fff"/>
          <circle cx="6" cy="14.5" r="1" fill="#fff"/>
        </svg>
      </li>
    </ul>
  </section>

  <section class="card card--back" aria-label="Business card back">
    <div class="back__rule"></div>
    <span class="back__mark"></span>
    <p class="back__name">Tobias Wrenfield</p>
  </section>
</main>
</body>
</html>
```